Gestaltung von Honigetiketten
Zielgruppe
Ich bin ein Imker, der im eigenen Restaurant seinen Honig ausstellen und verkaufen möchte.
Aufgabenstellung
Ich möchte exklusive und edle Honigetiketten die auffallen. Bevorzugt mit den Farben Gold und Schwarz, siehe meinem bisher gesehenen Favoriten im Anhang.
Nur das Logo selbst (Baum) soll übernommen werden Farbe kann variieren, ebenso die Schrift ist variabel.
Auf die Vorderseite des Honigetiketts soll zu lesen sein:
- Deutscher Honig
- Sommertracht
- 500g
- Logo und Name
Auf der Rückseite des Honigetiketts soll zu finden sein:
- freies Feld für Stempel für Namen und Adresse des Abfüllers
- freies Feld für das Mindesthaltbarkeitsdatum

```html
<!DOCTYPE html>
<html lang="de">
<head>
<meta charset="utf-8">
<title>Honigetikett – Sommertracht</title>
<link href="https://fonts.googleapis.com/css2?family=Raleway:wght@500&family=Uncial+Antiqua&family=Fondamento&family=Cormorant+Garamond:wght@500&display=swap" rel="stylesheet">
<style>
  :root {
    --backdrop: #ececec;
    --label-black: #050505;
    --comb-dark: #1c1a14;
    --comb-mid: #2e2a1f;
    --gold: #e3c33a;
    --white: #f7f5ee;
    --taupe: #7b7462;
  }
  html, body {
    margin: 0;
    padding: 0;
    width: 1200px;
    height: 1200px;
    overflow: hidden;
    background: var(--backdrop);
  }
  .canvas {
    position: relative;
    width: 1200px;
    height: 1200px;
  }
  .front-label {
    position: absolute;
    left: 50px;
    top: 244px;
    width: 1100px;
    height: 713px;
    display: block;
  }
  .label-title-small {
    font-family: "Raleway", sans-serif;
    font-weight: 500;
    font-size: 29px;
    letter-spacing: 6px;
    fill: var(--white);
  }
  .label-title-main {
    font-family: "Uncial Antiqua", serif;
    font-size: 62px;
    fill: var(--gold);
  }
  .brand-name {
    font-family: "Raleway", sans-serif;
    font-weight: 500;
    font-size: 17px;
    letter-spacing: 2px;
    fill: var(--gold);
  }
  .producer-name {
    font-family: "Fondamento", cursive;
    font-size: 18px;
    fill: var(--white);
  }
  .weight-text {
    font-family: "Cormorant Garamond", serif;
    font-weight: 500;
    font-size: 30px;
    fill: var(--white);
  }
</style>
</head>
<body>
<div class="canvas">
  <svg class="front-label" viewBox="0 0 795 515" xmlns="http://www.w3.org/2000/svg" aria-label="Honigetikett Vorderseite">
    <defs>
      <linearGradient id="combTone" x1="0" y1="0" x2="1" y2="1">
        <stop offset="0" stop-color="var(--comb-mid)"/>
        <stop offset="1" stop-color="var(--comb-dark)"/>
      </linearGradient>
    </defs>

    <rect class="label-ground" x="0" y="0" width="795" height="515" fill="var(--label-black)"/>

    <rect class="honeycomb-top" x="0" y="0" width="795" height="212" fill="url(#combTone)" role="img" aria-label="Goldbraunes Wabenmuster als Hintergrund im oberen Teil"/>
    <rect class="honeycomb-bottom" x="0" y="340" width="795" height="72" fill="url(#combTone)" role="img" aria-label="Goldbraunes Wabenmuster als Band im unteren Teil"/>

    <g class="brand-mark">
      <circle cx="378" cy="68" r="26" fill="var(--gold)"/>
      <text class="brand-name" x="378" y="124" text-anchor="middle">AHORNHOF</text>
    </g>

    <text class="label-title-small" x="318" y="262" text-anchor="middle">DEUTSCHER HONIG</text>
    <text class="label-title-main" x="392" y="326" text-anchor="middle">Sommertracht</text>

    <line class="divider" x1="315" y1="440" x2="478" y2="440" stroke="var(--gold)" stroke-width="3"/>

    <text class="producer-name" x="393" y="482" text-anchor="middle">Gasthof zum Ahorn-Brennersaal</text>

    <rect class="weight-box" x="638" y="443" width="117" height="72" fill="var(--taupe)"/>
    <text class="weight-text" x="696" y="488" text-anchor="middle">500 g</text>
  </svg>
</div>
</body>
</html>
```